Corvane CRM Sales Brochure

We need a sales brochure to be designed to help us promote our Veltrano C.R.M. (Customer Relationship Management) products and services. Designs aren't limited to just one side. We'd like to see professional, yet creative and fun design concepts incorporating the logo branding. Our target market will be both "White Collar" industry (Accountants / Solicitors / Business Insurance Agencies) as well as "Blue Collar" Industry (Manufacturing / Construction / Electricians). The final design should communicate our business as an experienced provider of Veltrano C.R.M. solutions. Attached files include Logo and Draft Content

```html
<!DOCTYPE html>
<html lang="en">
<head>
<meta charset="utf-8">
<title>Corvane CRM Sales Brochure</title>
<link href="https://fonts.googleapis.com/css2?family=Source+Sans+3:wght@400;600;700&display=swap" rel="stylesheet">
<style>
:root{
  --blue:#4ec3ef;
  --blue-deep:#1fa8df;
  --orange:#f2a31f;
  --ink:#1f2a36;
  --text:#2b2b2b;
  --dark:#3a3a3c;
  --paper:#ffffff;
  --stage:#e4e4e4;
}
*{margin:0;padding:0;box-sizing:border-box}
html,body{width:1200px;height:827px;overflow:hidden;background:var(--stage)}
body{font-family:"Source Sans 3",Arial,sans-serif;color:var(--text);position:relative}
.page{position:absolute;top:40px;width:520px;height:732px;background:var(--paper);overflow:hidden;box-shadow:0 2px 8px rgba(0,0,0,.18)}
.page--front{left:44px}
.page--back{left:636px}
.photo{position:absolute;left:17px;top:10px;width:481px;height:316px;border-radius:0 38px 0 38px}
.photo--worker{background:linear-gradient(120deg,#b9c4cc 0%,#8ea2b0 35%,#3f5f8c 60%,#c9d1d8 100%)}
.photo--meeting{background:linear-gradient(100deg,#f3f3f3 0%,#c9c0b6 35%,#a88a6e 65%,#e8e6e3 100%)}
.brand-tab{position:absolute;top:0;width:148px;height:117px;background:var(--paper);border-radius:0 0 6px 6px;display:flex;flex-direction:column;align-items:center;justify-content:center;gap:8px}
.page--front .brand-tab{left:30px}
.page--back .brand-tab{left:39px}
.brand-tab__square{width:26px;height:26px;background:var(--blue)}
.brand-tab__name{font-size:27px;font-weight:600;letter-spacing:2px;color:var(--dark)}
.badge{position:absolute;width:118px;height:118px;border-radius:50%;background:var(--orange);border:4px solid #fff;box-shadow:0 0 0 1px #e2a24a;display:flex;align-items:center;justify-content:center;text-align:center;color:#fff;font-weight:700;font-size:21px;line-height:1.1;letter-spacing:.3px;z-index:2}
.page--front .badge{left:383px;top:231px}
.page--back .badge{left:392px;top:238px;width:102px;height:102px;font-size:18px}
.headline{position:absolute;left:17px;top:337px;width:250px;font-size:16.5px;font-weight:700;line-height:1.17;color:var(--dark);text-transform:uppercase}
.headline em{font-style:normal;color:var(--blue)}
.body-col{position:absolute;left:17px;top:410px;width:226px;font-size:7.8px;line-height:1.3;text-align:justify;color:#222}
.body-col p+p{margin-top:10px}
.benefit-panel{position:absolute;left:261px;top:309px;width:259px;height:395px;background:var(--blue);border-radius:38px 0 0 0}
.benefit{position:absolute;left:14px;width:233px;font-size:8.2px;line-height:1.27;color:var(--ink);text-align:justify}
.benefit svg{float:left;margin:0 6px 2px 0}
.benefit--1{top:62px}
.benefit--2{top:178px}
.benefit--3{top:308px}
.benefit-rule{position:absolute;left:0;width:259px;height:1px;background:rgba(255,255,255,.6)}
.footer{position:absolute;left:0;bottom:0;width:520px;height:32px;background:var(--dark);display:flex;align-items:center;justify-content:space-between;padding:0 16px;color:#fff;font-size:10px;font-weight:700;letter-spacing:1px}
.footer span{display:flex;align-items:center;gap:5px}
.intro{position:absolute;left:19px;top:343px;width:484px;font-size:8px;line-height:1.3;text-align:justify;color:#222}
.service{position:absolute;left:0;width:281px;height:80px;background:var(--blue);border-radius:0 32px 32px 0;padding:10px 80px 0 19px;font-size:7.4px;line-height:1.3;color:var(--ink);text-align:justify}
.service h3{font-size:9.6px;font-weight:700;color:var(--ink);margin-bottom:2px;text-align:left}
.service h3 span{font-weight:400;color:#fff}
.service__icon{position:absolute;right:10px;top:12px;width:56px;height:56px;border-left:1px solid rgba(255,255,255,.75);display:flex;align-items:center;justify-content:flex-end}
.service--marketing{top:419px}
.service--sales{top:506px}
.service--support{top:599px}
.package{position:absolute;left:296px;top:419px;width:224px;height:264px;background:linear-gradient(160deg,#3b3b3d 0%,#5a5a5c 60%,#8a8a8c 100%);padding:14px 12px 0 17px;color:#fff;font-size:8.8px;line-height:1.25;border-radius:0 0 0 6px}
.package ul{list-style:none;margin-top:10px}
.package li{position:relative;padding-left:14px;margin-bottom:5.5px}
.package li::before{content:"";position:absolute;left:0;top:2px;width:7px;height:7px;border-radius:50%;background:var(--blue)}
.package .grid{display:grid;grid-template-columns:1fr 1fr}
.package p.extra{margin-top:12px;text-align:justify}
</style>
</head>
<body>

<section class="page page--front">
  <div class="photo photo--worker" role="img" aria-label="Smiling construction worker in hard hat using a laptop in a factory"></div>
  <div class="brand-tab"><div class="brand-tab__square"></div><div class="brand-tab__name">CORVANE</div></div>

  <h1 class="headline">Enhance your customer<br>experiences to <em>grow</em><br>your business faster</h1>

  <div class="body-col">
    <p>Leveraging existing customer value via a tailored Customer Relationship Management (CRM) system is far more cost effective than prospecting for new customers. In simple terms, CRM is a technological strategy focused on managing ongoing relationships with your customers to ensure they are provided with the information they seek to enable them to purchase at the time they choose.</p>
    <p>In a digitally connected world, customer purchase perceptions are forming pre, during and post their interaction with your brand. Customers are seeking to be satisfied with the quality of your products and services, but a complicated sales process or poor service engagement will worsen overall impressions typically resulting in the likelihood of no sales transactions.</p>
    <p>CRM is the art/act of developing a working relationship with your customers, where they feel a sense of individual importance. CRM solutions increase your profitability by streamlining administrative processes in your sales, marketing, and service divisions, and letting you focus on building and maintaining the customer relationships that matter. A strong CRM solution is a multifaceted platform where everything crucial to developing, improving, and retaining your customer relationships is stored.</p>
  </div>

  <div class="benefit-panel">
    <div class="benefit benefit--1">
      <svg width="36" height="28" viewBox="0 0 36 28" aria-hidden="true"><g fill="#fff"><rect x="0" y="16" width="4" height="12"/><rect x="6" y="10" width="4" height="18"/><path d="M22 14 L22 2 A12 12 0 1 1 12 20 Z"/><rect x="12" y="22" width="4" height="6"/></g></svg>
      Without the support of an integrated CRM solution, you may miss growth opportunities and lose revenue because you're not optimizing your operating processes or making the most of your customer relationships or sales leads.
    </div>
    <div class="benefit-rule" style="top:160px"></div>
    <div class="benefit benefit--2">
      <svg width="34" height="34" viewBox="0 0 34 34" aria-hidden="true"><g fill="#fff"><circle cx="17" cy="10" r="8"/><path d="M2 34 C2 22 32 22 32 34 Z"/></g></svg>
      Imagine misplacing customer contact information, only to learn that your delay resulted in losing your client to a competitor. Or, picture your top two salespeople pursuing the same prospect, resulting in an annoyed potential customer and some unfriendly, in-house competition. Without a centralized and automated CRM system, your people can lose track of customer interactions and miss business opportunities.
    </div>
    <div class="benefit-rule" style="top:290px"></div>
    <div class="benefit benefit--3">
      <svg width="34" height="32" viewBox="0 0 34 32" aria-hidden="true"><g fill="#fff"><rect x="0" y="22" width="5" height="10"/><rect x="8" y="17" width="5" height="15"/><rect x="16" y="19" width="5" height="13"/><rect x="24" y="11" width="5" height="21"/></g><path d="M1 16 L10 9 L18 12 L31 2" stroke="#fff" stroke-width="2.5" fill="none"/><path d="M25 1 L32 1 L32 8 Z" fill="#fff"/></svg>
      If you want a competitive advantage in your marketplace, a tailored CRM solution is the simple answer. CRM can take the burden of managing your customers. It enables automation of your customer management processes so you can focus on what's important: leading your business to succeed.
    </div>
  </div>

  <div class="badge">SIMPLER<br>SYSTEMS</div>

  <footer class="footer">
    <span><svg width="9" height="9" viewBox="0 0 10 10" aria-hidden="true"><circle cx="5" cy="5" r="5" fill="var(--blue)"/><rect x="2.5" y="3.2" width="5" height="3.6" fill="#fff"/></svg>support@corvane.com</span>
    <span><svg width="10" height="10" viewBox="0 0 10 10" aria-hidden="true"><circle cx="5" cy="5" r="4.3" stroke="var(--blue)" stroke-width="1.2" fill="none"/><path d="M3.4 3 L4.4 2.8 L4.8 4 L4.2 4.5 Q5 5.8 5.6 6 L6.1 5.4 L7.2 5.9 L7 6.9 Q4 7 3.4 3Z" fill="var(--blue)"/></svg>(07) 3040 5812</span>
    <span><svg width="9" height="9" viewBox="0 0 10 10" aria-hidden="true"><circle cx="5" cy="5" r="5" fill="var(--blue)"/><circle cx="5" cy="5" r="2.6" fill="none" stroke="#fff" stroke-width="1"/></svg>www.corvane.com</span>
  </footer>
</section>

<section class="page page--back">
  <div class="photo photo--meeting" role="img" aria-label="Two businesswomen talking at a wooden table with a laptop and coffee cup"></div>
  <div class="brand-tab"><div class="brand-tab__square"></div><div class="brand-tab__name">CORVANE</div></div>
  <div class="badge">SIMPLER<br>SYSTEMS</div>

  <p class="intro">Corvane are experts in tailored CRM systems to suit businesses and departments of all sizes across a wide range of Government, Commercial and Not-for-Profit industry sectors. Using the power of Veltrano Nexus 365 we are able to install and configure a flexible solution that's customizable to suit your specific requirements. You have the choice of a stand-alone application to meet the needs of a specific line of business or use multiple CRM tools that work together as a powerful integrated solution across marketing, sales and customer service.</p>

  <div class="service service--marketing">
    <h3>MARKETING: <span>ENHANCE &amp; NURTURE</span></h3>
    Generate multichannel marketing campaigns, foster sales-ready leads, and align your sales and marketing teams with planning and tracking tools that integrate with your existing apps and services.
    <div class="service__icon"><svg width="46" height="40" viewBox="0 0 46 40" aria-hidden="true"><g fill="none" stroke="#fff" stroke-width="2"><rect x="4" y="4" width="24" height="26" rx="2"/><path d="M10 36 H22 M16 30 V36"/><path d="M9 12 H23 M9 18 H19 M9 24 H21"/><path d="M32 10 L40 6 M32 17 H42 M32 24 L40 28"/></g></svg></div>
  </div>

  <div class="service service--sales">
    <h3>SALES: <span>ENGAGE &amp; CONNECT</span></h3>
    Go beyond sales automation to better understand customer needs, engage more effectively, and win more deals. Sell smarter with embedded insights, foster relationships, boost productivity and accelerate sales performance.
    <div class="service__icon"><svg width="48" height="48" viewBox="0 0 48 48" aria-hidden="true"><g stroke="#fff" stroke-width="2" fill="none"><circle cx="24" cy="24" r="11"/><path d="M24 13 V4 M24 35 V44 M13 24 H4 M35 24 H44 M16 16 L9 9 M32 32 L39 39 M32 16 L39 9 M16 32 L9 39"/></g><g fill="#fff"><circle cx="24" cy="4" r="3"/><circle cx="24" cy="44" r="3"/><circle cx="4" cy="24" r="3"/><circle cx="44" cy="24" r="3"/><circle cx="9" cy="9" r="2.5"/><circle cx="39" cy="39" r="2.5"/><circle cx="39" cy="9" r="2.5"/><circle cx="9" cy="39" r="2.5"/></g><text x="24" y="29" text-anchor="middle" font-size="14" font-weight="700" fill="#fff" font-family="Source Sans 3, sans-serif">$</text></svg></div>
  </div>

  <div class="service service--support">
    <h3>CUSTOMER SERVICE: <span>FOSTER &amp; SUPPORT</span></h3>
    Deliver guided, intelligent service and support on any channel with a unique ability to work with your existing systems. Empower customers and agents with the tools they need to ensure quick and accurate resolution, every time.
    <div class="service__icon"><svg width="40" height="46" viewBox="0 0 40 46" aria-hidden="true"><g fill="#fff"><circle cx="20" cy="16" r="9"/><path d="M4 46 C4 30 36 30 36 46 Z"/><rect x="6" y="13" width="5" height="9" rx="2"/><rect x="29" y="13" width="5" height="9" rx="2"/></g><path d="M8 14 C8 1 32 1 32 14 M31 22 Q30 28 22 28" stroke="#fff" stroke-width="2" fill="none"/></svg></div>
  </div>

  <div class="package">
    Foundation CRM solution $4,990 + GST<br>Inclusions;
    <ul class="grid">
      <li>Briefing</li><li>Configuration</li>
      <li>Setup</li><li>Live launch</li>
      <li>Installation</li><li>Training</li>
    </ul>
    <p class="extra">To further enhance the power of your Veltrano CRM solution we offer broader modules and services that include;</p>
    <ul>
      <li>Ongoing personalised support</li>
      <li>Customised coding and development</li>
      <li>Bespoke modules</li>
      <li>Broader integration across wider systems</li>
      <li>Customised reporting</li>
      <li>Data migration</li>
    </ul>
  </div>

  <footer class="footer">
    <span><svg width="9" height="9" viewBox="0 0 10 10" aria-hidden="true"><circle cx="5" cy="5" r="5" fill="var(--blue)"/><rect x="2.5" y="3.2" width="5" height="3.6" fill="#fff"/></svg>support@corvane.com</span>
    <span><svg width="10" height="10" viewBox="0 0 10 10" aria-hidden="true"><circle cx="5" cy="5" r="4.3" stroke="var(--blue)" stroke-width="1.2" fill="none"/><path d="M3.4 3 L4.4 2.8 L4.8 4 L4.2 4.5 Q5 5.8 5.6 6 L6.1 5.4 L7.2 5.9 L7 6.9 Q4 7 3.4 3Z" fill="var(--blue)"/></svg>(07) 3040 5812</span>
    <span><svg width="9" height="9" viewBox="0 0 10 10" aria-hidden="true"><circle cx="5" cy="5" r="5" fill="var(--blue)"/><circle cx="5" cy="5" r="2.6" fill="none" stroke="#fff" stroke-width="1"/></svg>www.corvane.com</span>
  </footer>
</section>

</body>
</html>
```